We are a Yacht Charter Broker servicing VIP clients on booking sailing catamarans and motor yacht...

We are looking for a wildly creative website to attract high net worth clients to work with us in booking their dream yacht vacation. A site that you think is 5 years ahead of its time. Sexy, modern and unique. Our company name is BRELLAVON. Our colors are navy blue and silver.
BLUE:
RGBB 0/44/92
CMYC 100/86/36/31
SILVER:
RGB 152/163/173
CMYK 43/29/25/0

HEX 98a3ad

Target Market(s)

High net worth people in need of white glove brokerage serving in finding and booking their dream yacht for a vacation of a lifetime.

Coding

Coded - Design and coding required

Number of Pages Required

1 page

Requirements
Must have
• Mobile friendly.
• Wildly creative and different. A website that we would expect to see 5 years from now.
• Pictures of yachts and or people on yachts. Palm tree landscapes.
• pictures of high end food related to the VIP yacht experience.
Nice to have
• Anything you feel would sell the yacht charter experience.
Should not have
• Nothing comes to mind.

```html
<!DOCTYPE html>
<html lang="en">
<head>
<meta charset="utf-8">
<title>BRELLAVON — Yacht Charter Broker</title>
<link rel="stylesheet" href="https://fonts.googleapis.com/css2?family=Open+Sans:ital,wght@0,300;0,400;0,600;0,700;1,400&family=Arimo:wght@400;700&display=swap">
<style>
  :root {
    --navy: #002c5c;
    --navy-deep: #0f2f5c;
    --silver: #98a3ad;
    --ink: #111111;
    --muted: #6b6f75;
    --rule: #d6d9dc;
    --white: #ffffff;
    --black: #000000;
    --footer-text: #d4d6d9;
  }
  * { box-sizing: border-box; margin: 0; padding: 0; }
  html, body { width: 1200px; height: 3322px; overflow: hidden; background: var(--white); }
  body { position: relative; font-family: "Open Sans", Arial, sans-serif; color: var(--ink); }
  .abs { position: absolute; }

  /* top bar */
  .top-bar { left: 0; top: 0; width: 1200px; height: 32px; background: var(--navy-deep); }
  .social { display: flex; gap: 4px; }
  .social span { width: 13px; height: 13px; background: var(--silver); display: block; }
  .top-bar .social { position: absolute; right: 28px; top: 9px; }

  /* brand wordmark */
  .brand { font-family: "Open Sans", Arial, sans-serif; font-weight: 300; color: var(--navy); letter-spacing: 5px; white-space: nowrap; }
  .brand-tag { font-family: "Open Sans", Arial, sans-serif; font-size: 9px; letter-spacing: 2px; color: var(--navy); font-weight: 600; white-space: nowrap; }
  .header-brand { left: 66px; top: 56px; font-size: 40px; }
  .header-tag { left: 126px; top: 104px; }
  .main-nav { right: 62px; top: 78px; display: flex; gap: 29px; font-size: 13px; font-weight: 600; color: var(--ink); }

  /* hero */
  .hero { left: 0; top: 145px; width: 1200px; height: 533px;
    background: linear-gradient(180deg, #8d9aa6 0%, #74869a 26%, #4d6580 48%, #34506e 66%, #2a425d 100%); }
  .hero-title { left: 63px; top: 232px; width: 820px; font-family: "Arimo", Arial, sans-serif; font-weight: 700; font-size: 54px; line-height: 62px; color: var(--white); }
  .hero-copy { left: 63px; top: 395px; width: 400px; font-family: "Arimo", Arial, sans-serif; font-size: 12.5px; line-height: 16px; color: var(--white); }
  .hero-cta { left: 63px; top: 502px; width: 145px; height: 40px; background: var(--white); color: var(--ink); font-family: "Arimo", Arial, sans-serif; font-weight: 700; font-size: 15px; display: flex; align-items: center; justify-content: center; }

  /* section headings */
  .section-title { font-family: "Open Sans", Arial, sans-serif; font-weight: 600; font-size: 30px; color: var(--ink); }
  .centre-title { left: 0; width: 1200px; text-align: center; }
  .centre-rule { left: 473px; width: 255px; height: 5px; background: var(--navy); }
  .centre-sub { left: 0; width: 1200px; text-align: center; font-size: 12px; letter-spacing: 2.5px; color: var(--muted); }

  /* about */
  .about-title { left: 63px; top: 720px; }
  .about-sub { left: 63px; top: 764px; font-size: 13px; letter-spacing: 2px; color: var(--ink); }
  .about-rule { left: 63px; top: 796px; width: 258px; height: 5px; background: var(--navy); }
  .about-copy { left: 63px; top: 822px; width: 480px; font-size: 11.5px; line-height: 13.5px; font-style: italic; letter-spacing: 2px; color: var(--muted); }
  .about-more { left: 63px; top: 942px; font-size: 16px; color: var(--ink); }
  .about-brand { left: 638px; top: 792px; font-size: 72px; letter-spacing: 9px; }
  .about-tag { left: 872px; top: 876px; font-size: 15px; letter-spacing: 4px; }
  .divider { left: 28px; top: 1016px; width: 1144px; height: 1px; background: var(--rule); }

  /* yachts */
  .slider-arrows { left: 1076px; top: 1166px; display: flex; gap: 9px; }
  .slider-arrows span { width: 28px; height: 20px; background: var(--navy); color: var(--white); font-size: 12px; display: flex; align-items: center; justify-content: center; }
  .yacht-card { top: 1193px; width: 357px; height: 222px; }
  .yacht-card.featured { background: linear-gradient(180deg, #3a5d8c 0%, #2b4d7e 45%, #20416f 70%, #1a3762 100%); }
  .yacht-card.open-water { background: linear-gradient(180deg, #4b78b8 0%, #93b3dc 30%, #e4ebf3 55%, #f4f6f8 64%, #3d7fb6 74%, #27679c 100%); }
  .yacht-card.coastline { background: linear-gradient(180deg, #3f6a44 0%, #5d8a5b 12%, #2c86bd 28%, #1f74ad 60%, #175f92 100%); }
  .card-overlay { position: absolute; inset: 0; display: flex; flex-direction: column; align-items: center; justify-content: center; color: var(--white); text-align: center; }
  .card-overlay strong { font-size: 20px; font-weight: 600; margin-top: 8px; }
  .card-overlay small { font-size: 10px; line-height: 13px; width: 200px; margin-top: 6px; }

  /* destinations */
  .destinations { left: 0; top: 1500px; width: 1200px; height: 369px; background: linear-gradient(100deg, #1d3f70 0%, #254a7d 45%, #30578a 70%, #22467a 100%); }
  .on-dark { color: var(--white); }
  .rule-light { background: var(--white); }
  .sub-light { color: #c7d2e0; }
  .search-field { top: 1672px; height: 56px; border: 2px solid var(--white); color: var(--white); font-size: 15px; font-weight: 600; letter-spacing: 2px; display: flex; align-items: flex-end; padding: 0 0 6px 10px; }
  .search-btn { left: 957px; top: 1672px; width: 186px; height: 54px; background: var(--white); color: var(--navy); font-size: 17px; font-weight: 600; display: flex; align-items: center; justify-content: center; }
  .dest-copy { left: 72px; top: 1749px; width: 1060px; font-size: 12px; line-height: 15px; font-style: italic; letter-spacing: 1px; color: var(--white); }

  /* gallery */
  .filters { left: 0; top: 2028px; width: 1200px; display: flex; justify-content: center; gap: 38px; font-size: 12px; letter-spacing: 2px; color: var(--muted); }
  .filters span { padding: 6px 0; }
  .filters .current { border: 2px solid var(--navy); padding: 4px 10px; color: var(--ink); }
  .shot { width: 287px; height: 199px; }
  .shot.family { left: 0; top: 2111px; background: linear-gradient(180deg, #6f9fcc 0%, #3f78ad 35%, #24588c 65%, #1c4873 100%); }
  .shot.deck { left: 307px; top: 2111px; background: linear-gradient(180deg, #7ea6cf 0%, #bcd2e6 35%, #eceeee 60%, #c9c2b4 100%); }
  .shot.seafood { left: 612px; top: 2111px; background: linear-gradient(180deg, #4f7fa8 0%, #9bb6c9 30%, #d8b48c 60%, #b0523f 100%); }
  .shot.party { left: 918px; top: 2111px; background: linear-gradient(180deg, #a9cbe8 0%, #d9e6f0 40%, #f2f3f2 65%, #d7d6d2 100%); }
  .shot.table { left: 0; top: 2330px; background: linear-gradient(180deg, #2f9bd0 0%, #66b8dc 30%, #c79a6a 65%, #8a6340 100%); }
  .shot.lounge { left: 307px; top: 2330px; background: linear-gradient(180deg, #5d8fc0 0%, #9dbcd8 35%, #eeeeec 65%, #d8d4cc 100%); }
  .shot.toast { left: 612px; top: 2330px; background: linear-gradient(180deg, #2f7fbf 0%, #5fa6d6 40%, #bfdcee 70%, #e9f1f5 100%); }
  .shot.sunset { left: 918px; top: 2330px; background: linear-gradient(180deg, #f0b878 0%, #d98f52 35%, #8c5a36 70%, #4a3020 100%); }
  .zoom-icon { left: 126px; top: 82px; }

  /* contact */
  .contact-title { top: 2597px; font-size: 31px; }
  .contact-rule { left: 481px; top: 2642px; width: 238px; height: 5px; background: #1d6fc2; }
  .field-label { font-size: 14px; font-style: italic; color: var(--muted); }
  .field-line { height: 1px; background: var(--rule); }
  .submit-btn { left: 90px; top: 2933px; width: 198px; height: 39px; background: var(--navy-deep); color: var(--white); font-family: "Arimo", Arial, sans-serif; font-weight: 700; font-size: 15px; display: flex; align-items: center; justify-content: center; }

  /* footer */
  .site-footer { left: 0; top: 3123px; width: 1200px; height: 199px; background: var(--black); }
  .footer-brand { left: 66px; top: 3174px; color: var(--white); font-size: 36px; }
  .footer-tag { left: 164px; top: 3220px; color: #bfc5cc; }
  .footer-col { top: 3158px; color: var(--white); }
  .footer-col h3 { font-size: 19px; font-weight: 600; margin-bottom: 8px; }
  .footer-col p { font-size: 15px; line-height: 22px; color: var(--footer-text); }
  .follow { left: 884px; top: 3164px; font-size: 16px; font-weight: 600; color: var(--white); }
  .footer-social { left: 884px; top: 3194px; gap: 5px; }
  .footer-social span { width: 17px; height: 17px; background: #a7adb3; }
  .footer-rule { left: 180px; top: 3296px; width: 840px; height: 1px; background: #444; }
  .footer-note { left: 0; top: 3302px; width: 1200px; text-align: center; font-size: 10px; letter-spacing: 1.5px; color: #aaa; font-style: italic; }
</style>
</head>
<body>

<div class="abs top-bar">
  <div class="social"><span></span><span></span><span></span><span></span></div>
</div>

<header>
  <div class="abs brand header-brand">BRELLAVON</div>
  <div class="abs brand-tag header-tag">YACHT CHARTER BROKER</div>
  <nav class="abs main-nav"><span>HOME</span><span>ABOUT US</span><span>YACHTS</span><span>DESTINATIONS</span><span>GALLERY</span><span>CONTACT US</span></nav>
</header>

<section>
  <div class="abs hero" role="img" aria-label="Guests swimming and lounging on a float beside a white motor yacht at sea"></div>
  <h1 class="abs hero-title">Lorem ipsum dolor sit amet, consectetur adipiscing elit.</h1>
  <p class="abs hero-copy">Integer eu pretium neque, at efficitur nunc. Etiam sed facilisis lorem, nec vehicula eros. Phasellus dictum massa odio, at congue mauris condimentum quis. Donec sed tellus nulla, ac pharetra eros. Aliquam bibendum vulputate suscipit.</p>
  <div class="abs hero-cta">Click Here!</div>
</section>

<section>
  <h2 class="abs section-title about-title">WHO WE ARE</h2>
  <div class="abs about-sub">Lorem ipsum dolor sit amet, consec</div>
  <div class="abs about-rule"></div>
  <p class="abs about-copy">Lorem ipsum dolor sit amet, consectetuer adipiscing elit, sed diam nonummy nibh euismod tincidunt ut laoreet dolore magna aliquam erat volutpat. Ut wisi enim ad minim veniam, quis nostrud exerci tation ullamcorper suscipit lobortis nisl ut aliquip ex ea commodo consequat. Duis autem vel eum iriure dolor in hendrerit in vulputate velit esse molestie consequat, vel illum dolore eu</p>
  <div class="abs about-more">more..</div>
  <div class="abs brand about-brand">BRELLAVON</div>
  <div class="abs brand-tag about-tag">YACHT CHARTER BROKER</div>
</section>
<div class="abs divider"></div>

<section>
  <h2 class="abs section-title centre-title" style="top:1070px">YACHTS</h2>
  <div class="abs centre-rule" style="top:1116px"></div>
  <p class="abs centre-sub" style="top:1136px">Lorem ipsum dolor sit amet, consectetur adipiscing elit. Praesent porttitor urna eu eleifend commodo.</p>
  <div class="abs slider-arrows"><span>&lt;</span><span>&gt;</span></div>
  <div class="abs yacht-card featured" style="left:63px" role="img" aria-label="Large white superyacht at anchor, tinted navy">
    <div class="card-overlay">
      <svg width="44" height="44" viewBox="0 0 44 44" fill="none" stroke="#fff" stroke-width="4"><circle cx="18" cy="18" r="13"/><line x1="28" y1="28" x2="41" y2="41" stroke-linecap="round"/></svg>
      <strong>Lorem Ipsun</strong>
      <small>Lorem ipsum dolor sit amet, consectetur adipisc ing elit, sed do eiusmod</small>
    </div>
  </div>
  <div class="abs yacht-card open-water" style="left:425px" role="img" aria-label="White motor yacht on calm water under a cloudy blue sky"></div>
  <div class="abs yacht-card coastline" style="left:786px" role="img" aria-label="Motor yacht cruising along a green island coastline"></div>
</section>

<section>
  <div class="abs destinations" role="img" aria-label="Yacht deck looking out to sea, tinted navy"></div>
  <h2 class="abs section-title centre-title on-dark" style="top:1533px">DESTINATIONS</h2>
  <div class="abs centre-rule rule-light" style="top:1582px"></div>
  <p class="abs centre-sub sub-light" style="top:1603px">Lorem ipsum dolor sit amet, consectetur adipiscing elit. Praesent porttitor urna eu eleifend commodo.</p>
  <div class="abs search-field" style="left:63px;width:274px">DESTIATNION</div>
  <div class="abs search-field" style="left:349px;width:210px">DATE</div>
  <div class="abs search-field" style="left:573px;width:154px">GUESTS</div>
  <div class="abs search-field" style="left:738px;width:207px">YACHT TYPE</div>
  <div class="abs search-btn">SHOW YACHTS</div>
  <p class="abs dest-copy">Lorem ipsum dolor sit amet, consectetuer adipiscing elit, sed diam nonummy nibh euismod tincidunt ut laoreet dolore magna aliquam erat volutpat. Ut wisi enim ad minim veniam, quis nostrud exerci tation ullamcorper suscipit lobortis nisl ut aliquip ex ea commodo consequat. Duis autem vel eum iriure dolor in hendrerit in vulputate velit esse molestie consequat, vel illum dolore eu</p>
</section>

<section>
  <h2 class="abs section-title centre-title" style="top:1899px">GALLERY</h2>
  <div class="abs centre-rule" style="top:1945px"></div>
  <p class="abs centre-sub" style="top:1964px">Lorem ipsum dolor sit amet, consectetur adipiscing elit. Praesent porttitor urna eu eleifend commodo.</p>
  <div class="abs filters"><span class="current">ALL</span><span>FAMILY</span><span>PARTY</span><span>FOOD</span><span>COUPLES</span><span>EVENTS</span><span>LAST</span></div>

  <div class="abs shot family" role="img" aria-label="Family relaxing on a yacht deck at sea">
    <svg class="abs zoom-icon" width="36" height="36" viewBox="0 0 36 36" fill="none" stroke="#fff" stroke-width="3"><circle cx="15" cy="15" r="11"/><line x1="23" y1="23" x2="33" y2="33"/><line x1="10" y1="15" x2="20" y2="15"/><line x1="15" y1="10" x2="15" y2="20"/></svg>
  </div>
  <div class="abs shot deck" role="img" aria-label="White yacht deck seating under blue sky"></div>
  <div class="abs shot seafood" role="img" aria-label="Seafood platter with candles and glasses on a deck table"></div>
  <div class="abs shot party" role="img" aria-label="Guests in white celebrating on a yacht deck"></div>
  <div class="abs shot table" role="img" aria-label="Food spread on a yacht table beside turquoise water"></div>
  <div class="abs shot lounge" role="img" aria-label="Couple relaxing on a yacht deck"></div>
  <div class="abs shot toast" role="img" aria-label="Champagne glasses on a sunny deck"></div>
  <div class="abs shot sunset" role="img" aria-label="Couple dining at sunset"></div>
</section>

<section>
  <h2 class="abs section-title centre-title contact-title">Contact Us</h2>
  <div class="abs contact-rule"></div>
  <div class="abs field-label" style="left:95px;top:2718px">Your name</div>
  <div class="abs field-line" style="left:88px;top:2753px;width:470px"></div>
  <div class="abs field-label" style="left:647px;top:2718px">Your name</div>
  <div class="abs field-line" style="left:644px;top:2753px;width:472px"></div>
  <div class="abs field-label" style="left:95px;top:2786px">Message</div>
  <div class="abs field-line" style="left:88px;top:2902px;width:1028px"></div>
  <div class="abs submit-btn">Submit</div>
</section>

<footer>
  <div class="abs site-footer"></div>
  <div class="abs brand footer-brand">BRELLAVON</div>
  <div class="abs brand-tag footer-tag">YACHT CHARTER BROKER</div>
  <div class="abs footer-col" style="left:385px"><h3>Links</h3><p>Link 1</p><p>Link 2</p><p>Link 3</p></div>
  <div class="abs footer-col" style="left:494px"><h3>Services</h3><p>serv 1</p><p>serv 2</p><p>serv 3</p></div>
  <div class="abs footer-col" style="left:653px"><h3>Lorem Ipsun</h3><p>Lorem 1</p><p>Lorem 2</p><p>Lorem 3</p></div>
  <div class="abs follow">FOLLOW US</div>
  <div class="abs social footer-social"><span></span><span></span><span></span><span></span></div>
  <div class="abs footer-rule"></div>
  <div class="abs footer-note">*Lorem ipsum dolor sit amet, consec</div>
</footer>

</body>
</html>
```